Real Estate Investment Company

Design Powerpoint slides are consistent with our logo, colors, and typeface. These Powerpoint slides will be used in all aspects of the business from live presentations to presentation decks available on a website or via email. Need to have different slide types created that allow for different types of slides such as cover pages, text heavy pages, image and chart heavy pages, multiple column pages, and mixed content pages.

Reason: to give additional time to get the design correct. I plan on making a selection in the next day or 2

Target Market(s)

Real Estate Investors

Industry/Entity Type

Investment

Other font styles liked:
• Consistent with logo

Requirements
Must have
• Our colors
• Our logo where possible
• Different slide designs of the same theme to allow for different types of slides such as cover pages, text heavy, picture heavy, and mixed content.
• Slides in both portrait and landscape orientation
Nice to have

```html
<!DOCTYPE html>
<html lang="en">
<head>
<meta charset="utf-8">
<title>Ridgeline Capital – Slide Theme</title>
<link rel="stylesheet" href="https://fonts.googleapis.com/css2?family=Montserrat:wght@500;600;700;800&family=Open+Sans:wght@400;600;700&display=swap">
<style>
:root{
  --navy:#2f3a85;
  --navy-dark:#232c66;
  --ink:#3a3a3a;
  --grey:#777;
  --light:#e9e9ee;
  --paper:#ffffff;
  --canvas:#f1f1f3;
  --red:#e0474c;
  --photo-warm:linear-gradient(135deg,#6b4a33,#b07a4a 55%,#3d2a1f);
  --photo-dark:linear-gradient(160deg,#3a3230,#2a2523 60%,#4a3d36);
  --photo-desk:linear-gradient(135deg,#f4f4f4,#c9c9cc 60%,#8d8f95);
}
*{box-sizing:border-box;margin:0;padding:0}
html,body{width:1200px;height:1200px;overflow:hidden;background:var(--canvas)}
.deck{
  width:1200px;height:1200px;padding:23px 26px;
  display:grid;grid-template-columns:repeat(4,281px);grid-template-rows:repeat(7,158px);gap:8px;
}
.slide{position:relative;overflow:hidden;background:var(--paper);box-shadow:0 1px 3px rgba(0,0,0,.18);font-family:"Open Sans",sans-serif;color:var(--ink)}
.slide > *{position:absolute}
.photo{display:block}
.warm{background:var(--photo-warm)}
.dark{background:var(--photo-dark)}
.desk{background:var(--photo-desk)}
.s-title{left:8px;top:6px;font:700 7.2px "Montserrat",sans-serif;color:var(--navy);letter-spacing:.1px}
.s-sub{left:8px;top:15px;font:700 4.4px "Montserrat",sans-serif;color:#222}
.mark{right:6px;top:5px}
.foot{left:8px;bottom:3px;font:3px "Open Sans",sans-serif;color:var(--grey)}
.pg{right:6px;bottom:3px;font:3px "Open Sans",sans-serif;color:var(--grey)}
.rule{left:0;right:0;bottom:9px;height:.6px;background:#ddd}
.para{font:3.5px/1.4 "Open Sans",sans-serif;color:var(--grey)}
.para.light{color:#e6e6e6}
.h{font:700 4.2px "Montserrat",sans-serif;color:#222;text-transform:uppercase}
.h.navy{color:var(--navy)}
.h.white{color:#fff}
.big{font:800 10px/1.1 "Montserrat",sans-serif;color:var(--navy);text-transform:uppercase}
.big.white{color:#fff}
.brand{display:flex;align-items:center;gap:2px;font:700 3.4px "Montserrat",sans-serif;color:var(--navy);letter-spacing:.3px;white-space:nowrap}
.brand i{display:block;width:4px;height:4px;background:var(--navy)}
.brand.lg{font-size:6px;gap:3px}
.brand.lg i{width:7px;height:7px}
.brand.white{color:#fff}
.brand.white i{background:#fff}
.cols{display:grid;gap:6px}
.dot{width:16px;height:16px;border-radius:50%;background:var(--navy);display:flex;align-items:center;justify-content:center}
.ring{width:14px;height:14px;border-radius:50%;border:.7px solid #aab;display:flex;align-items:center;justify-content:center}
table.data{border-collapse:collapse;font:3.4px "Open Sans",sans-serif;color:#555}
table.data th{background:var(--navy);color:#fff;font-weight:700;padding:1.6px 3px;text-align:left}
table.data td{padding:1.6px 3px;border-bottom:.5px solid #ddd}
table.data tr:nth-child(even) td{background:#f2f2f5}
table.data tr.total td{background:#dcdce4;font-weight:700}
</style>
</head>
<body>
<svg width="0" height="0" style="position:absolute" aria-hidden="true">
  <defs>
    <symbol id="ic-pin" viewBox="0 0 10 10"><path d="M5 1a3 3 0 0 1 3 3c0 2-3 5-3 5S2 6 2 4a3 3 0 0 1 3-3z" fill="none" stroke="currentColor" stroke-width=".8"/><circle cx="5" cy="4" r="1" fill="currentColor"/></symbol>
    <symbol id="ic-home" viewBox="0 0 10 10"><path d="M1.5 5 5 2l3.5 3M2.5 4.5V8.5h5V4.5" fill="none" stroke="currentColor" stroke-width=".8"/></symbol>
    <symbol id="ic-doc" viewBox="0 0 10 10"><rect x="2.5" y="1.5" width="5" height="7" fill="none" stroke="currentColor" stroke-width=".8"/><path d="M3.5 3.5h3M3.5 5h3M3.5 6.5h2" stroke="currentColor" stroke-width=".6"/></symbol>
    <symbol id="ic-user" viewBox="0 0 10 10"><circle cx="5" cy="3.5" r="1.8" fill="none" stroke="currentColor" stroke-width=".8"/><path d="M2 9a3 3 0 0 1 6 0" fill="none" stroke="currentColor" stroke-width=".8"/></symbol>
    <symbol id="ic-tool" viewBox="0 0 10 10"><path d="M2 8 7 3M6.5 1.5 8.5 3.5M2 2l6 6" stroke="currentColor" stroke-width=".9" fill="none"/></symbol>
    <symbol id="ic-dollar" viewBox="0 0 10 10"><path d="M6.8 3.2C6.3 2.5 3.2 2.3 3.2 3.8S6.8 5 6.8 6.4 3.7 7.8 3.1 6.8M5 1.5v7" fill="none" stroke="currentColor" stroke-width=".8"/></symbol>
    <symbol id="ic-bed" viewBox="0 0 10 10"><path d="M1.5 7.5V3M1.5 6h7v1.5M3 6V4.5h5.5V6" fill="none" stroke="currentColor" stroke-width=".8"/></symbol>
    <symbol id="ic-chat" viewBox="0 0 10 10"><path d="M1.5 2h7v4.5H4L2.5 8V6.5h-1z" fill="none" stroke="currentColor" stroke-width=".8"/></symbol>
    <symbol id="ic-card" viewBox="0 0 10 10"><rect x="1.5" y="2.5" width="7" height="5" fill="none" stroke="currentColor" stroke-width=".8"/><path d="M1.5 4h7" stroke="currentColor" stroke-width=".8"/></symbol>
    <symbol id="ic-key" viewBox="0 0 10 10"><circle cx="3.5" cy="6.5" r="1.8" fill="none" stroke="currentColor" stroke-width=".9"/><path d="m4.8 5.2 3.5-3.5M7 3l1 1" stroke="currentColor" stroke-width=".9" fill="none"/></symbol>
    <symbol id="ic-person" viewBox="0 0 6 14"><circle cx="3" cy="2" r="1.7" fill="currentColor"/><path d="M.6 4.5h4.8v5H4.4V14H1.6V9.5H.6z" fill="currentColor"/></symbol>
  </defs>
</svg>

<main class="deck">

<!-- 1 cover -->
<section class="slide">
  <div class="photo warm" role="img" aria-label="Warm living room interior with sofa and bookshelves" style="left:0;top:0;width:281px;height:95px"></div>
  <div class="brand lg" style="left:14px;top:116px">
    <i></i>RIDGELINE CAPITAL
  </div>
  <div class="big" style="left:120px;top:110px;font-size:10px">Presentation Title<br>Goes Here</div>
  <div class="h" style="left:120px;top:134px;font-size:4px;text-transform:none">Your Subtitle Goes Here</div>
</section>

<!-- 2 cover plain -->
<section class="slide">
  <div class="brand lg" style="left:22px;top:72px"><i></i>RIDGELINE CAPITAL</div>
  <div style="left:118px;top:58px;width:.7px;height:38px;background:#ccc"></div>
  <div class="big" style="left:126px;top:60px;font-size:11px">Presentation<br>Title Goes Here</div>
  <div class="h" style="left:126px;top:88px;font-size:4px;text-transform:none">Your Subtitle Goes Here</div>
</section>

<!-- 3 cover photo band -->
<section class="slide">
  <div class="photo dark" role="img" aria-label="Bright open-plan office kitchen with pendant lights" style="left:0;top:0;width:281px;height:148px"></div>
  <div style="left:0;top:95px;width:281px;height:42px;background:rgba(255,255,255,.92)"></div>
  <div style="left:12px;top:88px;width:54px;height:54px;border-radius:50%;background:#fff;border:2px solid #e6e6e6;display:flex;align-items:center;justify-content:center">
    <div class="brand" style="font-size:3.2px"><i></i>RIDGELINE CAPITAL</div>
  </div>
  <div class="big" style="left:96px;top:99px;font-size:8px">Presentation Title Goes Here</div>
  <p class="para" style="left:96px;top:110px;width:176px">Lorem ipsum dolor sit amet, consectetur adipiscing elit. Aliquam lacus justo, vulputate consequat laoreet eget, hendrerit in metus. Sed consectetur lorem mi, id faucibus urna posuere lacinia.</p>
  <div class="foot">www.ridgeline-capital.com</div><div class="pg">03</div>
</section>

<!-- 4 bullet grid -->
<section class="slide">
  <div class="s-title">PRESENTATION TITLE GOES HERE</div><div class="s-sub">Subtitle goes here</div>
  <div class="mark brand"><i></i>RIDGELINE CAPITAL</div>
  <div class="cols" style="left:8px;top:26px;width:266px;grid-template-columns:repeat(3,1fr);row-gap:9px">
    <div><div class="h navy">■ Bullet Heading</div><p class="para">Lorem ipsum dolor sit amet, consectetur adipiscing elit.</p></div>
    <div><div class="h navy">■ Bullet Heading</div><p class="para">Lorem ipsum dolor sit amet, consectetur adipiscing elit.</p></div>
    <div><div class="h navy">■ Bullet Heading</div><p class="para">Lorem ipsum dolor sit amet, consectetur adipiscing elit.</p></div>
    <div><div class="h navy">■ Bullet Heading</div><p class="para">Lorem ipsum dolor sit amet, consectetur adipiscing elit.</p></div>
    <div><div class="h navy">■ Bullet Heading</div><p class="para">Lorem ipsum dolor sit amet, consectetur adipiscing elit.</p></div>
    <div><div class="h navy">■ Bullet Heading</div><p class="para">Lorem ipsum dolor sit amet, consectetur adipiscing elit.</p></div>
    <div><div class="h navy">■ Bullet Heading</div><p class="para">Lorem ipsum dolor sit amet, consectetur adipiscing elit.</p></div>
    <div><div class="h navy">■ Bullet Heading</div><p class="para">Lorem ipsum dolor sit amet, consectetur adipiscing elit.</p></div>
    <div><div class="h navy">■ Bullet Heading</div><p class="para">Lorem ipsum dolor sit amet, consectetur adipiscing elit.</p></div>
    <div><div class="h navy">■ Bullet Heading</div><p class="para">Lorem ipsum dolor sit amet, consectetur adipiscing elit.</p></div>
    <div><div class="h navy">■ Bullet Heading</div><p class="para">Lorem ipsum dolor sit amet, consectetur adipiscing elit.</p></div>
    <div><div class="h navy">■ Bullet Heading</div><p class="para">Lorem ipsum dolor sit amet, consectetur adipiscing elit.</p></div>
  </div>
  <div class="rule"></div><div class="foot">www.ridgeline-capital.com</div><div class="pg">04</div>
</section>

<!-- 5 photo + navy panel -->
<section class="slide">
  <div class="s-title">PRESENTATION TITLE GOES HERE</div><div class="s-sub">Subtitle goes here</div>
  <div class="mark brand"><i></i>RIDGELINE CAPITAL</div>
  <div class="photo desk" role="img" aria-label="Desk with laptop, plant and coffee cup" style="left:0;top:28px;width:125px;height:52px"></div>
  <div style="left:125px;top:28px;width:156px;height:52px;background:var(--navy)"></div>
  <div class="h white" style="left:145px;top:38px;font-size:5px">Lorem Ipsum</div>
  <p class="para light" style="left:145px;top:46px;width:125px">Lorem ipsum dolor sit amet, consectetur adipiscing elit. Aliquam lacus justo, vulputate consequat laoreet eget, hendrerit in metus.</p>
  <div class="h navy" style="left:92px;top:88px;font-size:5px">Lorem Ipsum</div>
  <p class="para" style="left:8px;top:97px;width:264px">Lorem ipsum dolor sit amet, consectetur adipiscing elit. Aliquam lacus justo, vulputate consequat laoreet eget, hendrerit in metus. Sed consectetur lorem mi, id faucibus urna posuere lacinia. Proin a augue viverra, porttitor nulla at, facilisis lorem.</p>
  <div class="rule"></div><div class="foot">www.ridgeline-capital.com</div><div class="pg">05</div>
</section>

<!-- 6 split laptop -->
<section class="slide">
  <div class="brand lg" style="left:12px;top:14px"><i></i>RIDGELINE CAPITAL</div>
  <div class="big" style="left:12px;top:38px;font-size:8px">Presentation<br>Title Goes Here</div>
  <p class="para" style="left:12px;top:62px;width:72px">Lorem ipsum dolor sit amet, consectetur adipiscing elit. Aliquam lacus justo, vulputate consequat laoreet eget, hendrerit in metus. Sed consectetur lorem mi, id faucibus urna.</p>
  <p class="para" style="left:12px;top:96px;width:72px">Proin a augue viverra, porttitor nulla at, facilisis lorem. Suspendisse sed auctor tellus.</p>
  <div class="photo desk" role="img" aria-label="Hands working on a laptop showing charts" style="left:92px;top:0;width:189px;height:158px"></div>
</section>

<!-- 7 key point -->
<section class="slide">
  <div class="photo dark" role="img" aria-label="Office interior with wooden floor" style="left:0;top:0;width:281px;height:42px"></div>
  <div class="big white" style="left:0;right:0;top:14px;text-align:center;font-size:9px">Key Point</div>
  <div class="cols" style="left:10px;top:50px;width:262px;grid-template-columns:1fr 1fr;row-gap:10px">
    <div style="display:flex;gap:5px"><div class="ring" style="color:var(--navy)"><svg width="8" height="8"><use href="#ic-pin"/></svg></div><div><div class="h">Lorem ipsum dolor</div><p class="para">Lorem ipsum dolor sit amet, consectetur adipiscing elit. Aliquam lacus justo, vulputate.</p></div></div>
    <div style="display:flex;gap:5px"><div class="ring" style="color:var(--navy)"><svg width="8" height="8"><use href="#ic-home"/></svg></div><div><div class="h">Lorem ipsum dolor</div><p class="para">Lorem ipsum dolor sit amet, consectetur adipiscing elit. Aliquam lacus justo, vulputate.</p></div></div>
    <div style="display:flex;gap:5px"><div class="ring" style="color:var(--navy)"><svg width="8" height="8"><use href="#ic-doc"/></svg></div><div><div class="h">Lorem ipsum dolor</div><p class="para">Lorem ipsum dolor sit amet, consectetur adipiscing elit. Aliquam lacus justo, vulputate.</p></div></div>
    <div style="display:flex;gap:5px"><div class="ring" style="color:var(--navy)"><svg width="8" height="8"><use href="#ic-user"/></svg></div><div><div class="h">Lorem ipsum dolor</div><p class="para">Lorem ipsum dolor sit amet, consectetur adipiscing elit. Aliquam lacus justo, vulputate.</p></div></div>
  </div>
  <div class="rule"></div><div class="foot">www.ridgeline-capital.com</div><div class="pg">07</div>
</section>

<!-- 8 text + photo right -->
<section class="slide">
  <div class="s-title">PRESENTATION TITLE GOES HERE</div><div class="s-sub">Subtitle goes here</div>
  <div class="photo desk" role="img" aria-label="Desk with notebook, phone and keyboard" style="left:142px;top:0;width:139px;height:148px"></div>
  <div class="mark brand"><i></i>RIDGELINE CAPITAL</div>
  <div style="left:8px;top:30px;width:126px;display:flex;flex-direction:column;gap:6px">
    <div><div class="h">Lorem ipsum dolor</div><p class="para">Lorem ipsum dolor sit amet, consectetur adipiscing elit. Aliquam lacus justo, vulputate consequat laoreet eget, hendrerit in metus.</p></div>
    <div><div class="h">Lorem ipsum dolor</div><p class="para">Lorem ipsum dolor sit amet, consectetur adipiscing elit. Aliquam lacus justo, vulputate consequat laoreet eget, hendrerit in metus.</p></div>
    <div><div class="h">Lorem ipsum dolor</div><p class="para">Lorem ipsum dolor sit amet, consectetur adipiscing elit. Aliquam lacus justo, vulputate consequat laoreet eget, hendrerit in metus.</p></div>
  </div>
  <div class="rule"></div><div class="foot">www.ridgeline-capital.com</div><div class="pg">08</div>
</section>

<!-- 9 four columns -->
<section class="slide">
  <div class="s-title">PRESENTATION TITLE GOES HERE</div><div class="s-sub">Subtitle goes here</div>
  <div class="mark brand"><i></i>RIDGELINE CAPITAL</div>
  <p class="para" style="left:8px;top:24px;width:266px">Lorem ipsum dolor sit amet, consectetur adipiscing elit. Aliquam lacus justo, vulputate consequat laoreet eget, hendrerit in metus. Sed consectetur lorem mi, id faucibus urna posuere lacinia. Proin a augue viverra, porttitor nulla at, facilisis lorem. Suspendisse sed auctor tellus.</p>
  <div class="cols" style="left:8px;top:44px;width:266px;grid-template-columns:repeat(4,1fr);row-gap:6px">
    <div><div class="h">Lorem ipsum dolor</div><p class="para">Lorem ipsum dolor sit amet, consectetur adipiscing elit. Aliquam lacus justo, vulputate consequat.</p></div>
    <div><div class="h">Lorem ipsum dolor</div><p class="para">Lorem ipsum dolor sit amet, consectetur adipiscing elit. Aliquam lacus justo, vulputate consequat.</p></div>
    <div><div class="h">Lorem ipsum dolor</div><p class="para">Lorem ipsum dolor sit amet, consectetur adipiscing elit. Aliquam lacus justo, vulputate consequat.</p></div>
    <div><div class="h">Lorem ipsum dolor</div><p class="para">Lorem ipsum dolor sit amet, consectetur adipiscing elit. Aliquam lacus justo, vulputate consequat.</p></div>
    <div><p class="para">Lorem ipsum dolor sit amet, consectetur adipiscing elit. Aliquam lacus justo, vulputate consequat laoreet eget.</p></div>
    <div><p class="para">Lorem ipsum dolor sit amet, consectetur adipiscing elit. Aliquam lacus justo, vulputate consequat laoreet eget.</p></div>
    <div><p class="para">Lorem ipsum dolor sit amet, consectetur adipiscing elit. Aliquam lacus justo, vulputate consequat laoreet eget.</p></div>
    <div><p class="para">Lorem ipsum dolor sit amet, consectetur adipiscing elit. Aliquam lacus justo, vulputate consequat laoreet eget.</p></div>
  </div>
  <div class="rule"></div><div class="foot">www.ridgeline-capital.com</div><div class="pg">09</div>
</section>

<!-- 10 three columns -->
<section class="slide">
  <div class="s-title">PRESENTATION TITLE GOES HERE</div><div class="s-sub">Subtitle goes here</div>
  <div class="mark brand"><i></i>RIDGELINE CAPITAL</div>
  <p class="para" style="left:8px;top:24px;width:266px">Lorem ipsum dolor sit amet, consectetur adipiscing elit. Aliquam lacus justo, vulputate consequat laoreet eget, hendrerit in metus. Sed consectetur lorem mi, id faucibus urna posuere lacinia. Proin a augue viverra, porttitor nulla at, facilisis lorem.</p>
  <div class="cols" style="left:8px;top:44px;width:266px;grid-template-columns:repeat(3,1fr)">
    <div><div class="h">Lorem ipsum dolor</div><p class="para">Lorem ipsum dolor sit amet, consectetur adipiscing elit. Aliquam lacus justo, vulputate consequat laoreet eget, hendrerit in metus. Sed consectetur lorem mi, id faucibus urna posuere lacinia.</p><p class="para" style="margin-top:3px">Lorem ipsum dolor sit amet, consectetur adipiscing elit. Aliquam lacus justo, vulputate consequat.</p></div>
    <div><div class="h">Lorem ipsum dolor</div><p class="para">Lorem ipsum dolor sit amet, consectetur adipiscing elit. Aliquam lacus justo, vulputate consequat laoreet eget, hendrerit in metus. Sed consectetur lorem mi, id faucibus urna posuere lacinia.</p><p class="para" style="margin-top:3px">Lorem ipsum dolor sit amet, consectetur adipiscing elit. Aliquam lacus justo, vulputate consequat.</p></div>
    <div><div class="h">Lorem ipsum dolor</div><p class="para">Lorem ipsum dolor sit amet, consectetur adipiscing elit. Aliquam lacus justo, vulputate consequat laoreet eget, hendrerit in metus. Sed consectetur lorem mi, id faucibus urna posuere lacinia.</p><p class="para" style="margin-top:3px">Lorem ipsum dolor sit amet, consectetur adipiscing elit. Aliquam lacus justo, vulputate consequat.</p></div>
  </div>
  <div class="rule"></div><div class="foot">www.ridgeline-capital.com</div><div class="pg">10</div>
</section>

<!-- 11 dark + icon row -->
<section class="slide">
  <div class="photo dark" role="img" aria-label="Dark brick building facade" style="left:0;top:0;width:281px;height:158px"></div>
  <div class="big white" style="left:0;right:0;top:10px;text-align:center;font-size:8.5px">Lorem Ipsum</div>
  <p class="para light" style="left:50px;top:23px;width:182px;text-align:center">Lorem ipsum dolor sit amet, consectetur adipiscing elit. Aliquam lacus justo, vulputate consequat laoreet eget, hendrerit in metus. Sed consectetur lorem mi, id faucibus urna posuere lacinia.</p>
  <div style="left:0;top:78px;width:281px;height:80px;background:#fff"></div>
  <div class="cols" style="left:10px;top:52px;width:262px;grid-template-columns:repeat(5,1fr);justify-items:center;text-align:center">
    <div><div class="dot" style="width:20px;height:20px;margin:0 auto 14px;color:#fff"><svg width="10" height="10"><use href="#ic-user"/></svg></div><div class="h">Lorem ipsum</div><p class="para">Lorem ipsum dolor sit amet, consectetur elit.</p></div>
    <div><div class="dot" style="width:20px;height:20px;margin:0 auto 14px;color:#fff"><svg width="10" height="10"><use href="#ic-tool"/></svg></div><div class="h">Lorem ipsum</div><p class="para">Lorem ipsum dolor sit amet, consectetur elit.</p></div>
    <div><div class="dot" style="width:20px;height:20px;margin:0 auto 14px;color:#fff"><svg width="10" height="10"><use href="#ic-doc"/></svg></div><div class="h">Lorem ipsum</div><p class="para">Lorem ipsum dolor sit amet, consectetur elit.</p></div>
    <div><div class="dot" style="width:20px;height:20px;margin:0 auto 14px;color:#fff"><svg width="10" height="10"><use href="#ic-bed"/></svg></div><div class="h">Lorem ipsum</div><p class="para">Lorem ipsum dolor sit amet, consectetur elit.</p></div>
    <div><div class="dot" style="width:20px;height:20px;margin:0 auto 14px;color:#fff"><svg width="10" height="10"><use href="#ic-dollar"/></svg></div><div class="h">Lorem ipsum</div><p class="para">Lorem ipsum dolor sit amet, consectetur elit.</p></div>
  </div>
</section>

<!-- 12 devices -->
<section class="slide">
  <div class="photo dark" role="img" aria-label="Dark building facade" style="left:0;top:0;width:281px;height:86px"></div>
  <div class="big white" style="left:0;right:0;top:8px;text-align:center;font-size:8.5px">Lorem Ipsum</div>
  <svg style="left:0;top:20px" width="281" height="70" viewBox="0 0 281 70">
    <g font-family="Montserrat,sans-serif" font-weight="800" fill="#8a8a8a">
      <rect x="88" y="6" width="108" height="52" fill="#fff" stroke="#222" stroke-width="2"/>
      <text x="142" y="28" font-size="7" text-anchor="middle">WEBPAGE</text>
      <rect x="60" y="24" width="44" height="36" fill="#fff" stroke="#222" stroke-width="2"/>
      <text x="82" y="44" font-size="5.5" text-anchor="middle">WEBPAGE</text>
      <rect x="160" y="22" width="70" height="44" fill="#fff" stroke="#222" stroke-width="2"/>
      <text x="195" y="47" font-size="7" text-anchor="middle">WEBPAGE</text>
      <rect x="42" y="34" width="14" height="26" rx="2" fill="#fff" stroke="#222" stroke-width="1.5"/>
    </g>
  </svg>
  <div class="cols" style="left:10px;top:100px;width:262px;grid-template-columns:repeat(4,1fr);text-align:center">
    <div><div class="h">Lorem ipsum</div><p class="para">Lorem ipsum dolor sit amet, consectetur adipiscing elit.</p></div>
    <div><div class="h">Lorem ipsum</div><p class="para">Lorem ipsum dolor sit amet, consectetur adipiscing elit.</p></div>
    <div><div class="h">Lorem ipsum</div><p class="para">Lorem ipsum dolor sit amet, consectetur adipiscing elit.</p></div>
    <div><div class="h">Lorem ipsum</div><p class="para">Lorem ipsum dolor sit amet, consectetur adipiscing elit.</p></div>
  </div>
  <div class="rule"></div><div class="foot">www.ridgeline-capital.com</div><div class="pg">12</div>
</section>

<!-- 13 icon circles -->
<section class="slide">
  <div class="s-title">PRESENTATION TITLE GOES HERE</div><div class="s-sub">Subtitle goes here</div>
  <div class="mark brand"><i></i>RIDGELINE CAPITAL</div>
  <p class="para" style="left:8px;top:24px;width:266px">Lorem ipsum dolor sit amet, consectetur adipiscing elit. Aliquam lacus justo, vulputate consequat laoreet eget, hendrerit in metus. Sed consectetur lorem mi, id faucibus urna posuere lacinia. Proin a augue viverra, porttitor nulla at, facilisis lorem.</p>
  <div class="cols" style="left:8px;top:52px;width:266px;grid-template-columns:repeat(5,1fr);text-align:center">
    <div><div class="dot" style="width:28px;height:28px;margin:0 auto 8px;color:#fff"><svg width="12" height="12"><use href="#ic-card"/></svg></div><div class="h">Lorem ipsum</div><p class="para">Lorem ipsum dolor sit amet, consectetur elit.</p></div>
    <div><div class="dot" style="width:28px;height:28px;margin:0 auto 8px;color:#fff"><svg width="12" height="12"><use href="#ic-doc"/></svg></div><div class="h">Lorem ipsum</div><p class="para">Lorem ipsum dolor sit amet, consectetur elit.</p></div>
    <div><div class="dot" style="width:28px;height:28px;margin:0 auto 8px;color:#fff"><svg width="12" height="12"><use href="#ic-chat"/></svg></div><div class="h">Lorem ipsum</div><p class="para">Lorem ipsum dolor sit amet, consectetur elit.</p></div>
    <div><div class="dot" style="width:28px;height:28px;margin:0 auto 8px;color:#fff"><svg width="12" height="12"><use href="#ic-user"/></svg></div><div class="h">Lorem ipsum</div><p class="para">Lorem ipsum dolor sit amet, consectetur elit.</p></div>
    <div><div class="dot" style="width:28px;height:28px;margin:0 auto 8px;color:#fff"><svg width="12" height="12"><use href="#ic-home"/></svg></div><div class="h">Lorem ipsum</div><p class="para">Lorem ipsum dolor sit amet, consectetur elit.</p></div>
  </div>
  <div class="rule"></div><div class="foot">www.ridgeline-capital.com</div><div class="pg">13</div>
</section>

<!-- 14 screen mockup -->
<section class="slide">
  <div class="photo dark" role="img" aria-label="Dark building facade" style="left:0;top:0;width:281px;height:88px"></div>
  <div class="big white" style="left:120px;top:12px;font-size:8.5px">Lorem Ipsum</div>
  <p class="para light" style="left:120px;top:26px;width:150px">Lorem ipsum dolor sit amet, consectetur adipiscing elit. Aliquam lacus justo, vulputate consequat laoreet eget, hendrerit in metus. Sed consectetur lorem mi, id faucibus urna posuere lacinia.</p>
  <svg style="left:12px;top:40px" width="90" height="80" viewBox="0 0 90 80">
    <rect x="2" y="2" width="86" height="54" rx="2" fill="#1e1e1e"/>
    <rect x="6" y="6" width="78" height="44" fill="#3a4f8a"/>
    <text x="45" y="26" font-family="Open Sans,sans-serif" font-size="5" fill="#fff" text-anchor="middle">Your</text>
    <text x="45" y="35" font-family="Montserrat,sans-serif" font-weight="700" font-size="7" fill="#fff" text-anchor="middle">Screen</text>
    <text x="45" y="43" font-family="Open Sans,sans-serif" font-size="5" fill="#fff" text-anchor="middle">Mockup</text>
    <path d="M38 56h14l3 12H35z" fill="#cfcfcf"/><rect x="28" y="68" width="34" height="2" fill="#bbb"/>
  </svg>
  <div class="cols" style="left:116px;top:78px;width:160px;grid-template-columns:repeat(4,1fr);text-align:center">
    <div><div class="dot" style="width:18px;height:18px;margin:0 auto 6px;color:#fff"><svg width="9" height="9"><use href="#ic-user"/></svg></div><p class="para">Lorem ipsum dolor sit amet, consectetur.</p></div>
    <div><div class="dot" style="width:18px;height:18px;margin:0 auto 6px;color:#fff"><svg width="9" height="9"><use href="#ic-doc"/></svg></div><p class="para">Lorem ipsum dolor sit amet, consectetur.</p></div>
    <div><div class="dot" style="width:18px;height:18px;margin:0 auto 6px;color:#fff"><svg width="9" height="9"><use href="#ic-card"/></svg></div><p class="para">Lorem ipsum dolor sit amet, consectetur.</p></div>
    <div><div class="dot" style="width:18px;height:18px;margin:0 auto 6px;color:#fff"><svg width="9" height="9"><use href="#ic-chat"/></svg></div><p class="para">Lorem ipsum dolor sit amet, consectetur.</p></div>
  </div>
</section>

<!-- 15 team -->
<section class="slide">
  <div class="photo dark" role="img" aria-label="Dark building facade" style="left:0;top:0;width:281px;height:82px"></div>
  <div class="big white" style="left:0;right:0;top:16px;text-align:center;font-size:8.5px">Meet Our Team</div>
  <div class="cols" style="left:22px;top:56px;width:238px;grid-template-columns:repeat(4,1fr);text-align:center">
    <div><div class="photo warm" role="img" aria-label="Team member portrait" style="width:28px;height:28px;border-radius:50%;border:1.5px solid #fff;margin:0 auto 6px"></div><div class="h">Lorem ipsum</div><p class="para">Lorem ipsum dolor sit amet, consectetur elit. Aliquam lacus.</p></div>
    <div><div class="photo warm" role="img" aria-label="Team member portrait" style="width:28px;height:28px;border-radius:50%;border:1.5px solid #fff;margin:0 auto 6px"></div><div class="h">Lorem ipsum</div><p class="para">Lorem ipsum dolor sit amet, consectetur elit. Aliquam lacus.</p></div>
    <div><div class="photo warm" role="img" aria-label="Team member portrait" style="width:28px;height:28px;border-radius:50%;border:1.5px solid #fff;margin:0 auto 6px"></div><div class="h">Lorem ipsum</div><p class="para">Lorem ipsum dolor sit amet, consectetur elit. Aliquam lacus.</p></div>
    <div><div class="photo warm" role="img" aria-label="Team member portrait" style="width:28px;height:28px;border-radius:50%;border:1.5px solid #fff;margin:0 auto 6px"></div><div class="h">Lorem ipsum</div><p class="para">Lorem ipsum dolor sit amet, consectetur elit. Aliquam lacus.</p></div>
  </div>
</section>

<!-- 16 stat cards -->
<section class="slide">
  <div class="s-title">PRESENTATION TITLE GOES HERE</div><div class="s-sub">Subtitle goes here</div>
  <div class="mark brand"><i></i>RIDGELINE CAPITAL</div>
  <div class="cols" style="left:12px;top:32px;width:258px;height:104px;grid-template-columns:repeat(4,1fr);gap:5px;text-align:center">
    <div style="background:#eeeef2;border:.6px solid #ccc;padding:8px 4px"><div class="dot" style="width:24px;height:24px;margin:0 auto 8px;font:700 5.5px Montserrat,sans-serif;color:#fff">10K</div><p class="para">Lorem ipsum dolor sit amet, consectetur adipiscing elit. Aliquam lacus justo.</p></div>
    <div style="background:#eeeef2;border:.6px solid #ccc;padding:8px 4px"><div class="dot" style="width:24px;height:24px;margin:0 auto 8px;font:700 5.5px Montserrat,sans-serif;color:#fff">15K</div><p class="para">Lorem ipsum dolor sit amet, consectetur adipiscing elit. Aliquam lacus justo.</p></div>
    <div style="background:#eeeef2;border:.6px solid #ccc;padding:8px 4px"><div class="dot" style="width:24px;height:24px;margin:0 auto 8px;font:700 5.5px Montserrat,sans-serif;color:#fff">20K</div><p class="para">Lorem ipsum dolor sit amet, consectetur adipiscing elit. Aliquam lacus justo.</p></div>
    <div style="background:#eeeef2;border:.6px solid #ccc;padding:8px 4px"><div class="dot" style="width:24px;height:24px;margin:0 auto 8px;font:700 5.5px Montserrat,sans-serif;color:#fff">25K</div><p class="para">Lorem ipsum dolor sit amet, consectetur adipiscing elit. Aliquam lacus justo.</p></div>
  </div>
  <div class="rule"></div><div class="foot">www.ridgeline-capital.com</div><div class="pg">16</div>
</section>

<!-- 17 steps -->
<section class="slide">
  <div class="s-title">PRESENTATION TITLE GOES HERE</div><div class="s-sub">Subtitle goes here</div>
  <div class="mark brand"><i></i>RIDGELINE CAPITAL</div>
  <p class="para" style="left:8px;top:28px;width:104px">Lorem ipsum dolor sit amet, consectetur adipiscing elit. Aliquam lacus justo, vulputate consequat laoreet eget, hendrerit in metus. Sed consectetur lorem mi, id faucibus urna posuere lacinia. Proin a augue viverra, porttitor nulla at, facilisis lorem.</p>
  <p class="para" style="left:8px;top:74px;width:104px">Lorem ipsum dolor sit amet, consectetur adipiscing elit. Aliquam lacus justo, vulputate consequat laoreet eget, hendrerit in metus. Sed consectetur lorem mi, id faucibus urna posuere lacinia.</p>
  <svg style="left:118px;top:24px" width="160" height="124" viewBox="0 0 160 124" font-family="Montserrat,sans-serif" font-weight="700">
    <circle cx="48" cy="60" r="18" fill="#fff" stroke="#ddd" stroke-width="4"/>
    <text x="48" y="59" font-size="4" text-anchor="middle" fill="#333">LOREM</text>
    <text x="48" y="64" font-size="4" text-anchor="middle" fill="#333">IPSUM</text>
    <path d="M48 42a18 18 0 0 1 18 16" fill="none" stroke="var(--navy)" stroke-width="5"/>
    <path d="M66 62a18 18 0 0 1-12 15" fill="none" stroke="var(--red)" stroke-width="5"/>
    <path d="M42 77a18 18 0 0 1-12-19" fill="none" stroke="var(--navy-dark)" stroke-width="5"/>
    <rect x="32" y="14" width="22" height="18" rx="9" fill="var(--navy)"/>
    <text x="43" y="21" font-size="3.5" fill="#fff" text-anchor="middle">STEP</text><text x="43" y="28" font-size="6" fill="#fff" text-anchor="middle">01</text>
    <rect x="70" y="52" width="22" height="18" rx="9" fill="var(--red)"/>
    <text x="81" y="59" font-size="3.5" fill="#fff" text-anchor="middle">STEP</text><text x="81" y="66" font-size="6" fill="#fff" text-anchor="middle">02</text>
    <rect x="32" y="90" width="22" height="18" rx="9" fill="var(--navy-dark)"/>
    <text x="43" y="97" font-size="3.5" fill="#fff" text-anchor="middle">STEP</text><text x="43" y="104" font-size="6" fill="#fff" text-anchor="middle">03</text>
    <rect x="58" y="16" width="24" height="7" rx="3.5" fill="var(--navy)"/><text x="70" y="21" font-size="4" fill="#fff" text-anchor="middle">Lorem</text>
    <rect x="96" y="54" width="24" height="7" rx="3.5" fill="var(--red)"/><text x="108" y="59" font-size="4" fill="#fff" text-anchor="middle">Lorem</text>
    <rect x="58" y="92" width="24" height="7" rx="3.5" fill="var(--navy-dark)"/><text x="70" y="97" font-size="4" fill="#fff" text-anchor="middle">Lorem</text>
    <g font-family="Open Sans,sans-serif" font-weight="400" font-size="3.3" fill="#777">
      <text x="58" y="29">Lorem ipsum dolor sit amet,</text><text x="58" y="33">consectetur adipiscing.</text>
      <text x="96" y="67">Lorem ipsum dolor sit amet,</text><text x="96" y="71">consectetur adipiscing.</text>
      <text x="58" y="105">Lorem ipsum dolor sit amet,</text><text x="58" y="109">consectetur adipiscing.</text>
    </g>
  </svg>
  <div class="rule"></div><div class="foot">www.ridgeline-capital.com</div><div class="pg">17</div>
</section>

<!-- 18 photo + list -->
<section class="slide">
  <div class="photo dark" role="img" aria-label="Office kitchen interior with pendant lights" style="left:0;top:0;width:160px;height:158px;background:linear-gradient(150deg,#5a3e2e,#9a6c46 50%,#2e2420)"></div>
  <div style="left:0;top:100px;width:160px;height:58px;background:rgba(47,58,133,.92)"></div>
  <div class="big white" style="left:8px;top:106px;font-size:7px">Presentation Title Goes Here</div>
  <p class="para light" style="left:8px;top:118px;width:146px">Lorem ipsum dolor sit amet, consectetur adipiscing elit. Aliquam lacus justo, vulputate consequat laoreet eget, hendrerit in metus. Sed consectetur lorem mi, id faucibus urna.</p>
  <div class="mark brand"><i></i>RIDGELINE CAPITAL</div>
  <div style="left:166px;top:20px;width:108px;display:flex;flex-direction:column;gap:8px">
    <div style="display:flex;gap:4px;color:var(--navy)"><svg width="9" height="9" style="flex:none"><use href="#ic-user"/></svg><div><div class="h" style="color:#222">Lorem ipsum</div><p class="para">Lorem ipsum dolor sit amet, consectetur adipiscing elit. Aliquam lacus justo.</p></div></div>
    <div style="display:flex;gap:4px;color:var(--navy)"><svg width="9" height="9" style="flex:none"><use href="#ic-tool"/></svg><div><div class="h" style="color:#222">Lorem ipsum</div><p class="para">Lorem ipsum dolor sit amet, consectetur adipiscing elit. Aliquam lacus justo.</p></div></div>
    <div style="display:flex;gap:4px;color:var(--navy)"><svg width="9" height="9" style="flex:none"><use href="#ic-card"/></svg><div><div class="h" style="color:#222">Lorem ipsum</div><p class="para">Lorem ipsum dolor sit amet, consectetur adipiscing elit. Aliquam lacus justo.</p></div></div>
    <div style="display:flex;gap:4px;color:var(--navy)"><svg width="9" height="9" style="flex:none"><use href="#ic-bed"/></svg><div><div class="h" style="color:#222">Lorem ipsum</div><p class="para">Lorem ipsum dolor sit amet, consectetur adipiscing elit. Aliquam lacus justo.</p></div></div>
  </div>
</section>

<!-- 19 team + clients -->
<section class="slide">
  <div class="photo dark" role="img" aria-label="Dark building facade" style="left:0;top:0;width:281px;height:70px"></div>
  <div class="big white" style="left:0;right:0;top:14px;text-align:center;font-size:8.5px">Meet Our Team</div>
  <p class="para light" style="left:50px;top:27px;width:182px;text-align:center">Lorem ipsum dolor sit amet, consectetur adipiscing elit. Aliquam lacus justo, vulputate consequat laoreet eget, hendrerit in metus. Sed consectetur lorem mi, id faucibus urna posuere lacinia.</p>
  <div style="left:8px;top:98px;width:265px;display:flex;align-items:center;gap:5px;font:700 6.5px Montserrat,sans-serif;color:#cfcfd4">
    <span style="color:#bbb">‹</span>
    <span style="flex:1;height:24px;border:.6px solid #ddd;display:flex;align-items:center;justify-content:center;text-align:center;line-height:1">Client<br>Logo</span>
    <span style="flex:1;height:24px;border:.6px solid #ddd;display:flex;align-items:center;justify-content:center;text-align:center;line-height:1">Client<br>Logo</span>
    <span style="flex:1;height:24px;border:.6px solid #ddd;display:flex;align-items:center;justify-content:center;text-align:center;line-height:1">Client<br>Logo</span>
    <span style="flex:1;height:24px;border:.6px solid #ddd;display:flex;align-items:center;justify-content:center;text-align:center;line-height:1">Client<br>Logo</span>
    <span style="flex:1;height:24px;border:.6px solid #ddd;display:flex;align-items:center;justify-content:center;text-align:center;line-height:1">Client<br>Logo</span>
    <span style="color:#bbb">›</span>
  </div>
</section>

<!-- 20 quadrant -->
<section class="slide">
  <div class="s-title">PRESENTATION TITLE GOES HERE</div><div class="s-sub">Subtitle goes here</div>
  <div class="mark brand"><i></i>RIDGELINE CAPITAL</div>
  <svg style="left:105px;top:28px" width="72" height="72" viewBox="0 0 72 72">
    <path d="M34 0A34 34 0 0 0 0 34h34z" fill="var(--navy)"/>
    <path d="M38 0a34 34 0 0 1 34 34H38z" fill="var(--navy)"/>
    <path d="M0 38a34 34 0 0 0 34 34V38z" fill="var(--navy)"/>
    <path d="M38 72a34 34 0 0 0 34-34H38z" fill="var(--navy)"/>
    <g color="#fff"><use href="#ic-key" x="12" y="12" width="14" height="14"/><use href="#ic-tool" x="46" y="12" width="14" height="14"/><use href="#ic-card" x="12" y="46" width="14" height="14"/><use href="#ic-bed" x="46" y="46" width="14" height="14"/></g>
  </svg>
  <div style="left:38px;top:34px;width:62px;text-align:right"><div class="h navy">Title here</div><p class="para">Entrepreneurial activities differ substantially depending on the type.</p></div>
  <div style="left:38px;top:72px;width:62px;text-align:right"><div class="h navy">Title here</div><p class="para">Entrepreneurial activities differ substantially depending on the type.</p></div>
  <div style="left:184px;top:34px;width:64px"><div class="h navy">Title here</div><p class="para">Entrepreneurial activities differ substantially depending on the type.</p></div>
  <div style="left:184px;top:72px;width:64px"><div class="h navy">Title here</div><p class="para">Entrepreneurial activities differ substantially depending on the type.</p></div>
  <div class="rule"></div><div class="foot">www.ridgeline-capital.com</div><div class="pg">20</div>
</section>

<!-- 21 donuts -->
<section class="slide">
  <div class="s-title">PRESENTATION TITLE GOES HERE</div><div class="s-sub">Subtitle goes here</div>
  <div class="mark brand"><i></i>RIDGELINE CAPITAL</div>
  <svg style="left:0;top:24px" width="281" height="120" viewBox="0 0 281 120" font-family="Montserrat,sans-serif">
    <g transform="translate(72 52)" fill="none" stroke-width="8">
      <circle r="28" stroke="#c9cce0"/>
      <circle r="28" stroke="var(--navy)" stroke-dasharray="110 176" transform="rotate(-90)"/>
      <circle r="28" stroke="#6e78b8" stroke-dasharray="30 176" stroke-dashoffset="-110" transform="rotate(-90)"/>
      <circle r="28" stroke="#222" stroke-dasharray="14 176" stroke-dashoffset="-140" transform="rotate(-90)"/>
    </g>
    <text x="72" y="56" font-size="10" font-weight="600" fill="#555" text-anchor="middle">2016</text>
    <g transform="translate(196 52)" fill="none" stroke-width="8">
      <circle r="28" stroke="#c9cce0"/>
      <circle r="28" stroke="var(--navy)" stroke-dasharray="124 176" transform="rotate(-90)"/>
      <circle r="28" stroke="#6e78b8" stroke-dasharray="20 176" stroke-dashoffset="-124" transform="rotate(-90)"/>
      <circle r="28" stroke="#222" stroke-dasharray="12 176" stroke-dashoffset="-144" transform="rotate(-90)"/>
    </g>
    <text x="196" y="56" font-size="10" font-weight="600" fill="#555" text-anchor="middle">2018</text>
    <g font-family="Open Sans,sans-serif" font-size="3.4" fill="#777">
      <text x="72" y="19" text-anchor="middle">34%</text><text x="108" y="56">20%</text><text x="36" y="64" text-anchor="end">12%</text>
      <text x="196" y="19" text-anchor="middle">15%</text><text x="232" y="56">50%</text><text x="160" y="64" text-anchor="end">12%</text>
    </g>
    <g font-family="Open Sans,sans-serif" font-size="3.6" fill="#555">
      <rect x="42" y="95" width="3" height="3" fill="var(--navy)"/><text x="47" y="98">Lorem</text>
      <rect x="60" y="95" width="3" height="3" fill="#6e78b8"/><text x="65" y="98">Ipsum</text>
      <rect x="78" y="95" width="3" height="3" fill="#222"/><text x="83" y="98">Lorem</text>
      <rect x="96" y="95" width="3" height="3" fill="#c9cce0"/><text x="101" y="98">Ipsum</text>
      <rect x="166" y="95" width="3" height="3" fill="var(--navy)"/><text x="171" y="98">Lorem</text>
      <rect x="184" y="95" width="3" height="3" fill="#6e78b8"/><text x="189" y="98">Ipsum</text>
      <rect x="202" y="95" width="3" height="3" fill="#222"/><text x="207" y="98">Lorem</text>
      <rect x="220" y="95" width="3" height="3" fill="#c9cce0"/><text x="225" y="98">Ipsum</text>
    </g>
  </svg>
  <div class="rule"></div><div class="foot">www.ridgeline-capital.com</div><div class="pg">21</div>
</section>

<!-- 22 line chart -->
<section class="slide">
  <div class="s-title">PRESENTATION TITLE GOES HERE</div>
  <div class="mark brand"><i></i>RIDGELINE CAPITAL</div>
  <svg style="left:0;top:18px" width="281" height="128" viewBox="0 0 281 128" font-family="Open Sans,sans-serif" font-size="3.6" fill="#777">
    <g stroke="#e3e3e3" stroke-width=".5">
      <line x1="20" y1="14" x2="250" y2="14"/><line x1="20" y1="32" x2="250" y2="32"/><line x1="20" y1="50" x2="250" y2="50"/><line x1="20" y1="68" x2="250" y2="68"/><line x1="20" y1="86" x2="250" y2="86"/>
    </g>
    <line x1="20" y1="104" x2="250" y2="104" stroke="#999" stroke-width=".6"/>
    <text x="14" y="106" text-anchor="end">0</text><text x="14" y="88" text-anchor="end">1</text><text x="14" y="70" text-anchor="end">2</text><text x="14" y="52" text-anchor="end">3</text><text x="14" y="34" text-anchor="end">4</text><text x="14" y="16" text-anchor="end">5</text>
    <text x="20" y="112" text-anchor="middle">0</text><text x="46" y="112" text-anchor="middle">0.5</text><text x="71" y="112" text-anchor="middle">1</text><text x="97" y="112" text-anchor="middle">1.5</text><text x="122" y="112" text-anchor="middle">2</text><text x="148" y="112" text-anchor="middle">2.5</text><text x="173" y="112" text-anchor="middle">3</text><text x="199" y="112" text-anchor="middle">3.5</text><text x="224" y="112" text-anchor="middle">4</text><text x="250" y="112" text-anchor="middle">4.5</text>
    <g fill="none" stroke-width="1">
      <path d="M71 41C110 50 160 80 224 60" stroke="var(--navy)"/>
      <path d="M71 64C110 58 160 30 224 86" stroke="#222"/>
      <path d="M71 20C120 30 150 95 224 45" stroke="#5a63a8"/>
    </g>
    <g fill="#222"><circle cx="71" cy="41" r="1.2"/><circle cx="71" cy="64" r="1.2"/><circle cx="71" cy="20" r="1.2"/><circle cx="224" cy="60" r="1.2"/><circle cx="224" cy="86" r="1.2"/><circle cx="224" cy="45" r="1.2"/></g>
    <line x1="100" y1="121" x2="106" y2="121" stroke="var(--navy)"/><text x="108" y="122">Series 1</text>
    <line x1="128" y1="121" x2="134" y2="121" stroke="#222"/><text x="136" y="122">Series 2</text>
    <line x1="156" y1="121" x2="162" y2="121" stroke="#5a63a8"/><text x="164" y="122">Series 3</text>
  </svg>
  <div class="rule"></div><div class="foot">www.ridgeline-capital.com</div><div class="pg">22</div>
</section>

<!-- 23 bar chart -->
<section class="slide">
  <div class="s-title">PRESENTATION TITLE GOES HERE</div>
  <div class="mark brand"><i></i>RIDGELINE CAPITAL</div>
  <svg style="left:0;top:18px" width="281" height="128" viewBox="0 0 281 128" font-family="Open Sans,sans-serif" font-size="3.4" fill="#777">
    <g stroke="#e6e6e6" stroke-width=".5"><line x1="44" y1="10" x2="44" y2="104"/><line x1="92" y1="10" x2="92" y2="104"/><line x1="140" y1="10" x2="140" y2="104"/><line x1="188" y1="10" x2="188" y2="104"/><line x1="236" y1="10" x2="236" y2="104"/></g>
    <text x="40" y="40" text-anchor="end">September</text><text x="40" y="84" text-anchor="end">October</text>
    <rect x="44" y="18" width="70" height="5" fill="var(--navy)"/><rect x="44" y="24" width="82" height="5" fill="#6e78b8"/><rect x="44" y="30" width="55" height="5" fill="#222"/><rect x="44" y="36" width="120" height="5" fill="#bbb"/><rect x="44" y="42" width="96" height="5" fill="#2c3a6e"/>
    <rect x="44" y="62" width="90" height="5" fill="var(--navy)"/><rect x="44" y="68" width="64" height="5" fill="#6e78b8"/><rect x="44" y="74" width="108" height="5" fill="#222"/><rect x="44" y="80" width="170" height="5" fill="#bbb"/><rect x="44" y="86" width="138" height="5" fill="#2c3a6e"/>
    <text x="44" y="112" text-anchor="middle">0</text><text x="92" y="112" text-anchor="middle">50</text><text x="140" y="112" text-anchor="middle">100</text><text x="188" y="112" text-anchor="middle">150</text><text x="236" y="112" text-anchor="middle">200</text>
    <g><rect x="70" y="119" width="3" height="3" fill="var(--navy)"/><text x="75" y="122">Lorem</text><rect x="96" y="119" width="3" height="3" fill="#6e78b8"/><text x="101" y="122">Ipsum</text><rect x="122" y="119" width="3" height="3" fill="#222"/><text x="127" y="122">Lorem</text><rect x="148" y="119" width="3" height="3" fill="#bbb"/><text x="153" y="122">Ipsum</text><rect x="174" y="119" width="3" height="3" fill="#2c3a6e"/><text x="179" y="122">Lorem</text></g>
  </svg>
  <div class="rule"></div><div class="foot">www.ridgeline-capital.com</div><div class="pg">23</div>
</section>

<!-- 24 progress rings -->
<section class="slide">
  <div class="s-title">PRESENTATION TITLE GOES HERE</div><div class="s-sub">Subtitle goes here</div>
  <div class="mark brand"><i></i>RIDGELINE CAPITAL</div>
  <svg style="left:0;top:30px" width="281" height="54" viewBox="0 0 281 54" font-family="Montserrat,sans-serif" font-weight="700" font-size="7.5" text-anchor="middle" fill="#222">
    <g fill="none" stroke-width="4">
      <circle cx="46" cy="24" r="18" stroke="#ddd"/><circle cx="46" cy="24" r="18" stroke="var(--navy)" stroke-dasharray="90.5 113" transform="rotate(-90 46 24)"/>
      <circle cx="109" cy="24" r="18" stroke="#ddd"/><circle cx="109" cy="24" r="18" stroke="#5a63a8" stroke-dasharray="55.4 113" transform="rotate(-90 109 24)"/>
      <circle cx="172" cy="24" r="18" stroke="#ddd"/><circle cx="172" cy="24" r="18" stroke="#111" stroke-dasharray="101.8 113" transform="rotate(-90 172 24)"/>
      <circle cx="235" cy="24" r="18" stroke="#ddd"/><circle cx="235" cy="24" r="18" stroke="#777" stroke-dasharray="34 113" transform="rotate(-90 235 24)"/>
    </g>
    <text x="46" y="27">80%</text><text x="109" y="27">49%</text><text x="172" y="27">90%</text><text x="235" y="27">30%</text>
    <g font-weight="600" font-size="5.5" fill="#666"><text x="46" y="53">$908</text><text x="109" y="53">$522</text><text x="172" y="53">$984</text><text x="235" y="53">$357</text></g>
  </svg>
  <div class="cols" style="left:18px;top:88px;width:246px;grid-template-columns:repeat(4,1fr);text-align:center">
    <p class="para">Lorem ipsum dolor sit amet, consectetur adipiscing elit. Aliquam lacus justo, vulputate.</p>
    <p class="para">Lorem ipsum dolor sit amet, consectetur adipiscing elit. Aliquam lacus justo, vulputate.</p>
    <p class="para">Lorem ipsum dolor sit amet, consectetur adipiscing elit. Aliquam lacus justo, vulputate.</p>
    <p class="para">Lorem ipsum dolor sit amet, consectetur adipiscing elit. Aliquam lacus justo, vulputate.</p>
  </div>
  <div class="rule"></div><div class="foot">www.ridgeline-capital.com</div><div class="pg">24</div>
</section>

<!-- 25 table -->
<section class="slide">
  <div class="s-title">PRESENTATION TITLE GOES HERE</div><div class="s-sub">Subtitle goes here</div>
  <div class="mark brand"><i></i>RIDGELINE CAPITAL</div>
  <table class="data" style="position:absolute;left:10px;top:30px;width:261px">
    <tr><th>Title</th><th>Jan</th><th>Feb</th><th>Mar</th><th>Apr</th><th>May</th><th>June</th><th>July</th></tr>
    <tr><td>Lorem</td><td>xxx</td><td>xxx</td><td>xxx</td><td>xxx</td><td>xxx</td><td>xxx</td><td>xxx</td></tr>
    <tr><td>Lorem</td><td>xxx</td><td>xxx</td><td>xxx</td><td>xxx</td><td>xxx</td><td>xxx</td><td>xxx</td></tr>
    <tr><td>Lorem</td><td>xxx</td><td>xxx</td><td>xxx</td><td>xxx</td><td>xxx</td><td>xxx</td><td>xxx</td></tr>
    <tr><td>Lorem</td><td>xxx</td><td>xxx</td><td>xxx</td><td>xxx</td><td>xxx</td><td>xxx</td><td>xxx</td></tr>
    <tr><td>Lorem</td><td>xxx</td><td>xxx</td><td>xxx</td><td>xxx</td><td>xxx</td><td>xxx</td><td>xxx</td></tr>
    <tr><td>Lorem</td><td>xxx</td><td>xxx</td><td>xxx</td><td>xxx</td><td>xxx</td><td>xxx</td><td>xxx</td></tr>
    <tr><td>Lorem</td><td>xxx</td><td>xxx</td><td>xxx</td><td>xxx</td><td>xxx</td><td>xxx</td><td>xxx</td></tr>
    <tr class="total"><td>TOTAL</td><td>xxx</td><td>xxx</td><td>xxx</td><td>xxx</td><td>xxx</td><td>xxx</td><td>xxx</td></tr>
  </table>
  <div class="rule"></div><div class="foot">www.ridgeline-capital.com</div><div class="pg">25</div>
</section>

<!-- 26 pictogram -->
<section class="slide">
  <div class="s-title">PRESENTATION TITLE GOES HERE</div><div class="s-sub">Subtitle goes here</div>
  <div class="mark brand"><i></i>RIDGELINE CAPITAL</div>
  <p class="para" style="left:8px;top:24px;width:266px">Lorem ipsum dolor sit amet, consectetur adipiscing elit. Aliquam lacus justo, vulputate consequat laoreet eget, hendrerit in metus. Sed consectetur lorem mi, id faucibus urna posuere lacinia. Proin a augue viverra, porttitor nulla at, facilisis lorem.</p>
  <svg style="left:22px;top:48px" width="250" height="96" viewBox="0 0 250 96" font-family="Montserrat,sans-serif" font-weight="800" font-size="11">
    <g color="var(--navy)">
      <use href="#ic-person" x="0" y="2" width="14" height="34"/><use href="#ic-person" x="16" y="2" width="14" height="34"/><use href="#ic-person" x="32" y="2" width="14" height="34"/><use href="#ic-person" x="48" y="2" width="14" height="34"/><use href="#ic-person" x="64" y="2" width="14" height="34"/><use href="#ic-person" x="80" y="2" width="14" height="34"/><use href="#ic-person" x="96" y="2" width="14" height="34"/><use href="#ic-person" x="112" y="2" width="14" height="34"/>
      <use href="#ic-person" x="0" y="52" width="14" height="34"/><use href="#ic-person" x="16" y="52" width="14" height="34"/><use href="#ic-person" x="32" y="52" width="14" height="34"/><use href="#ic-person" x="48" y="52" width="14" height="34"/><use href="#ic-person" x="64" y="52" width="14" height="34"/><use href="#ic-person" x="80" y="52" width="14" height="34"/>
    </g>
    <g color="#c6c9dc">
      <use href="#ic-person" x="128" y="2" width="14" height="34"/><use href="#ic-person" x="144" y="2" width="14" height="34"/>
      <use href="#ic-person" x="96" y="52" width="14" height="34"/><use href="#ic-person" x="112" y="52" width="14" height="34"/><use href="#ic-person" x="128" y="52" width="14" height="34"/><use href="#ic-person" x="144" y="52" width="14" height="34"/>
    </g>
    <text x="168" y="24" fill="var(--navy)">= 80%</text>
    <text x="168" y="74" fill="var(--navy)">= 60%</text>
  </svg>
  <div class="rule"></div><div class="foot">www.ridgeline-capital.com</div><div class="pg">26</div>
</section>

<!-- 27 quote navy -->
<section class="slide">
  <div class="photo" role="img" aria-label="Looking up at a tall building, tinted navy" style="left:0;top:0;width:281px;height:158px;background:radial-gradient(circle at 50% 60%,#4a55a0,#2f3a85 50%,#1f275e)"></div>
  <svg style="left:22px;top:58px" width="44" height="36" viewBox="0 0 44 36"><path d="M3 3h24v16H12l-6 6v-6H3z" fill="none" stroke="#fff" stroke-width="2.4"/><path d="M31 11h10v15h-3v5l-5-5H17v-4" fill="none" stroke="#fff" stroke-width="2.4"/></svg>
  <div class="big white" style="left:80px;top:58px;font-size:7.5px">Presentation Title Goes Here</div>
  <p class="para light" style="left:80px;top:70px;width:180px">Lorem ipsum dolor sit amet, consectetur adipiscing elit. Aliquam lacus justo, vulputate consequat laoreet eget, hendrerit in metus. Sed consectetur lorem mi, id faucibus urna posuere lacinia.</p>
</section>

<!-- 28 thank you -->
<section class="slide">
  <div class="photo" role="img" aria-label="Dim interior with wooden table and bookshelves" style="left:0;top:0;width:281px;height:158px;background:linear-gradient(160deg,#4a3a40,#3b3440 50%,#6a4a36)"></div>
  <div class="brand lg white" style="left:0;right:0;top:40px;justify-content:center"><i></i>RIDGELINE CAPITAL</div>
  <div class="big white" style="left:0;right:0;top:58px;text-align:center;font-size:11px">Thank You</div>
  <p class="para light" style="left:60px;top:76px;width:162px;text-align:center">Lorem ipsum dolor sit amet, consectetur adipiscing elit. Aliquam lacus justo, vulputate consequat laoreet eget, hendrerit in metus. Sed consectetur lorem mi, id faucibus urna posuere.</p>
</section>

</main>
</body>
</html>
```